Helicopter company requires newspaper ad

"Ridgeline Aviators" is an agricultural helicopter company based in Victoria, Australia. We need an advert design for use in newspapers and also possibly social media. Our company specialises in using a helicopter for various agricultural work such as Spraying weeds ("Cropdusting"), spreading fertiliser. This advert will be targeted at farmers in our service area, Our customers are mainly dairy and cow farmers and our services are aimed at increasing their farm productivity. The final design should inform potential and existing customers about our services and the benefits of them. I will attach files of our logo and some existing advertising material for guidance. We would like the ad to feature the blue and green colours in our logo Please feel free to view our website and facebook page to see more about what we do. www.ridgelineaviators.com.au Some text we would like included Spraying: -Accurate -Time Efficient -Zero crop damage -Cost efficient Fertiliser Spreading: -Accurate, Pattern-tested equipment -Zero crop damage or wheel marks -Ability to load product out of a truck, bin or bulk bags -Cost effective, Prices from $32 per hectare depending on spread rate The final advert size should be 195 mm wide x 186 mm high Thanks :)

Target Market(s)

Farmers, Agriculture Industry

Industry/Entity Type

Agribusiness

Colors

Designer to choose colors to be used in the design.

Requirements
Must have
• Phone number 0491 635 087
• The text included in the decription, or variations of this

```html
<!DOCTYPE html>
<html lang="en">
<head>
<meta charset="utf-8">
<title>Ridgeline Aviators – Agricultural Helicopter Services</title>
<link href="https://fonts.googleapis.com/css2?family=League+Spartan:wght@700&family=Open+Sans:wght@400;700;800&display=swap" rel="stylesheet">
<style>
  :root {
    --brand-blue: #1474c4;
    --brand-green: #8cc63f;
    --ink: #1f1f1f;
    --heading-ink: #474747;
    --paper: #ffffff;
  }
  * { margin: 0; padding: 0; box-sizing: border-box; }
  html, body { width: 1200px; height: 1144px; overflow: hidden; background: var(--paper); }
  .ad {
    position: relative;
    width: 1200px;
    height: 1144px;
    background: var(--paper);
    font-family: "Open Sans", Arial, sans-serif;
    color: var(--ink);
    overflow: hidden;
  }
  .ad__art { position: absolute; inset: 0; width: 1200px; height: 1144px; }
  .brand {
    position: absolute;
    left: 90px;
    top: 60px;
    width: 200px;
    text-align: center;
    color: var(--brand-blue);
  }
  .brand__name {
    font-weight: 800;
    font-size: 30px;
    line-height: 32px;
  }
  .brand__phone {
    margin-top: 10px;
    font-weight: 800;
    font-size: 22px;
    line-height: 28px;
    white-space: nowrap;
  }
  .headline {
    position: absolute;
    left: 0;
    top: 376px;
    width: 1200px;
    text-align: center;
    font-family: "League Spartan", "Futura", sans-serif;
    font-weight: 700;
    font-size: 68px;
    line-height: 80px;
    letter-spacing: 0.12em;
    text-indent: 0.12em;
    white-space: nowrap;
    color: var(--paper);
  }
  .service { position: absolute; }
  .service--spraying { left: 123px; top: 838px; }
  .service--fertiliser { left: 594px; top: 726px; }
  .service__title {
    font-weight: 700;
    font-size: 29px;
    line-height: 44px;
    color: var(--heading-ink);
    margin-bottom: 10px;
  }
  .service__list { list-style: none; }
  .service__list li {
    position: relative;
    font-size: 30px;
    line-height: 54px;
    white-space: nowrap;
  }
  .service__list li::before {
    content: "";
    position: absolute;
    left: -22px;
    top: 23px;
    width: 9px;
    height: 9px;
    border-radius: 50%;
    background: var(--ink);
  }
</style>
</head>
<body>
<main class="ad">
  <svg class="ad__art" viewBox="0 0 1200 1144">
    <defs>
      <linearGradient id="photoTone" x1="0" y1="0" x2="0" y2="1">
        <stop offset="0" stop-color="#6a8299"/>
        <stop offset="0.42" stop-color="#8fa0b0"/>
        <stop offset="0.52" stop-color="#c3ccd2"/>
        <stop offset="0.62" stop-color="#7f8a79"/>
        <stop offset="0.8" stop-color="#56613f"/>
        <stop offset="1" stop-color="#3f4a30"/>
      </linearGradient>
    </defs>
    <polygon class="hero-photo" role="img" aria-label="Photo of a crop-spraying helicopter flying low over green pasture, boom spraying mist beneath a cloudy blue sky"
      points="0,269 969,0 1200,0 1200,540 0,802" fill="url(#photoTone)"/>
    <polygon class="accent-green" points="557,89 877,0 969,0 557,114" fill="var(--brand-green)"/>
    <polygon class="accent-blue" points="0,802 1200,540 1200,568 0,830" fill="var(--brand-blue)"/>
  </svg>

  <div class="brand">
    <div class="brand__name">Ridgeline Aviators</div>
    <div class="brand__phone">0491 635 087</div>
  </div>

  <h1 class="headline">AGRICULTURAL HELICOPTER<br>SERVICES</h1>

  <section class="service service--fertiliser">
    <h2 class="service__title">FERTILISER SPREADING :</h2>
    <ul class="service__list">
      <li>Accurate, Pattern-tested equipment</li>
      <li>Zero crop damage or wheel marks</li>
      <li>Ability to load product out of a truck,<br>bin or bulk bags</li>
      <li>Prices from $32 per hectare depending<br>on spread rate</li>
    </ul>
  </section>

  <section class="service service--spraying">
    <h2 class="service__title">SPRAYING :</h2>
    <ul class="service__list">
      <li>Accurate</li>
      <li>Time Efficient</li>
      <li>Zero Crop damage</li>
      <li>Cost Efficient</li>
    </ul>
  </section>
</main>
</body>
</html>
```